Carrying bags for customer visit

I am looking to make a carrying case that can be used to carry small presents, gifts, our brochure (20 inch X20 inch) and sometimes our samples (which are printed circuit boards that have a size of 24X15). The case should look elegant, show our company logo and our slogan "PCB is our business". You can try to download our logo from our web site www.tarnvolt.com. I want a contemporary and cool feel of the carrying case that can be any materials. I prefer to use recyclable materials that reflects our company's business philosophy of practicing sustanbility. Also I would like to add Chinese name “锦泰电路(东莞)有限公司" in the bag.
Updates

Need extra days to review

Target Market(s)

Corporate customers who will come into contact with our companies

Colors

Designer to choose colors to be used in the design.

Requirements
Must have
• It has to be attractive and people wanting to use them on a regular basis. Therefore, the logo display and our slogan should be subtle. I want the carrying bags not to be very expensive to produce.

```html
<!DOCTYPE html>
<html lang="en">
<head>
<meta charset="utf-8">
<title>Tarnvolt Carrying Bag – Front Panel</title>
<link rel="stylesheet" href="https://fonts.googleapis.com/css2?family=Open+Sans:wght@700;800&family=Noto+Sans+SC:wght@400&display=swap">
<style>
  :root {
    --canvas-bg: #eeeeee;
    --panel-light: #fbfbfb;
    --panel-mid: #e6e6e6;
    --handle: #c9c9c9;
    --brand-green: #1f5a3a;
    --ink: #111111;
    --rule: #9a9a9a;
  }
  html, body {
    margin: 0;
    padding: 0;
    width: 1200px;
    height: 900px;
    overflow: hidden;
    background: var(--canvas-bg);
  }
  .canvas {
    position: relative;
    width: 1200px;
    height: 900px;
  }
  .bag-handles {
    position: absolute;
    left: 420px;
    top: 70px;
    width: 360px;
    height: 150px;
  }
  .bag-front {
    position: absolute;
    left: 420px;
    top: 200px;
    width: 360px;
    height: 620px;
    box-shadow: 0 18px 40px rgba(0,0,0,0.12);
  }
  .quilt-texture {
    position: absolute;
    inset: 0;
    background: radial-gradient(ellipse at 50% 40%, var(--panel-light) 0%, var(--panel-mid) 100%);
  }
  .brand-block {
    position: absolute;
    left: 0;
    right: 0;
    top: 205px;
    text-align: center;
  }
  .brand-name {
    font-family: "Open Sans", sans-serif;
    font-weight: 800;
    font-size: 44px;
    letter-spacing: 2px;
    color: var(--brand-green);
    line-height: 1;
  }
  .brand-rule {
    width: 180px;
    height: 1px;
    margin: 10px auto 0;
    background: var(--rule);
  }
  .slogan {
    margin-top: 16px;
    font-family: "Open Sans", sans-serif;
    font-weight: 700;
    font-size: 17px;
    color: var(--ink);
    letter-spacing: 0.3px;
  }
  .company-cn {
    position: absolute;
    left: 0;
    right: 0;
    top: 488px;
    text-align: center;
    font-family: "Noto Sans SC", sans-serif;
    font-weight: 400;
    font-size: 15px;
    color: var(--ink);
  }
</style>
</head>
<body>
  <main class="canvas">
    <svg class="bag-handles" viewBox="0 0 360 150" aria-hidden="true">
      <path d="M95 150 C95 40 150 10 185 10 C225 10 250 50 250 150" fill="none" stroke="var(--handle)" stroke-width="6" stroke-linecap="round"/>
      <path d="M120 150 C120 70 160 45 195 45 C235 45 270 80 275 150" fill="none" stroke="var(--handle)" stroke-width="6" stroke-linecap="round"/>
    </svg>
    <section class="bag-front">
      <div class="quilt-texture" role="img" aria-label="Light grey quilted diamond pattern covering the bag front"></div>
      <div class="brand-block">
        <div class="brand-name">TARNVOLT</div>
        <div class="brand-rule"></div>
        <div class="slogan">IS OUR BUSINESS</div>
      </div>
      <div class="company-cn">锦泰电路(东莞)有限公司</div>
    </section>
  </main>
</body>
</html>
```